We would like to design a logo, letter head, and business card.  

We have beauty colleges in the Kansas City Missouri USA area that have been around for 55 years.  We teach hair, skin and nail tech programs to students. Most of our students are female between the age of 18-30. 

• I appologize for failing to provide details on our addresses. We have 3 locations all with the same phone number.

Atelier of Marwick 4180 NE County Rd 9 Blue Springs MO 64027

Atelier of Marwick 3190 Pellham Kansas City MO 64152

Atelier of Marwick 17340 Cedar Knoll Blvd Grandview Mo 64139

Phone: (816) 555-0148

• Doug Marwick

President

4180 NE County Rd 9

Blue Springs MO 64027

(816) 555-0148

doug@zq-tress.example

Target Market(s)

18-30 Years Old

Industry/Entity Type

Business

Logo Text

Atelier of Marwick Beauty College

Requirements
Must have
• Atelier of Marwick Beauty College

```html
<!DOCTYPE html>
<html lang="en">
<head>
<meta charset="utf-8">
<title>Atelier of Marwick Beauty College – Stationery</title>
<link href="https://fonts.googleapis.com/css2?family=Cormorant+Garamond:wght@600&family=Roboto+Condensed:wght@400;700&display=swap" rel="stylesheet">
<style>
  :root {
    --purple: #4b0aa3;
    --gold: #f0aa00;
    --ink: #555555;
    --frame: #8a8a8a;
    --rule: #9a9a9a;
    --paper: #ffffff;
  }
  * { margin: 0; padding: 0; box-sizing: border-box; }
  html, body {
    width: 1200px; height: 1091px; overflow: hidden;
    background: var(--paper);
  }
  body { position: relative; font-family: "Roboto Condensed", "Arial Narrow", sans-serif; color: var(--ink); }

  .wordmark {
    font-family: "Cormorant Garamond", Georgia, serif;
    font-weight: 600;
    color: var(--purple);
    text-align: center;
    line-height: 1.05;
  }

  /* Standalone logo */
  .logo-showcase {
    position: absolute; left: 81px; top: 135px; width: 264px; height: 168px;
    display: flex; align-items: center; justify-content: center;
  }
  .logo-showcase .wordmark { font-size: 38px; }

  /* Business card */
  .business-card {
    position: absolute; left: 67px; top: 367px; width: 295px; height: 168px;
    border: 1px solid var(--frame); background: var(--paper); overflow: hidden;
    text-align: center;
  }
  .business-card .wordmark { margin-top: 18px; font-size: 15px; }
  .card-name { margin-top: 14px; font-size: 10px; color: var(--purple); line-height: 1; }
  .card-role { margin-top: 3px; font-size: 7.5px; color: var(--purple); line-height: 1; }
  .card-mobile { margin-top: 3px; font-size: 6.5px; line-height: 1; }
  .card-rule { width: 220px; height: 0; border-top: 1px solid var(--rule); margin: 5px auto 0; }
  .card-company { margin-top: 5px; font-size: 6.5px; font-weight: 700; color: var(--purple); line-height: 1; }
  .card-contact { font-size: 5.6px; line-height: 9.3px; margin-top: 2px; }
  .card-arc { position: absolute; left: 0; bottom: 0; width: 295px; height: 10px; display: block; }

  /* Letterhead */
  .letterhead {
    position: absolute; left: 395px; top: 21px; width: 692px; height: 978px;
    border: 1px solid var(--frame); background: var(--paper); overflow: hidden;
  }
  .letterhead-logo {
    position: absolute; left: 0; right: 0; top: 60px;
    display: flex; justify-content: center;
  }
  .letterhead-logo .wordmark { font-size: 30px; }
  .letterhead-footer {
    position: absolute; left: 0; right: 0; top: 890px; text-align: center;
  }
  .footer-company { font-size: 14px; font-weight: 700; color: var(--purple); line-height: 1; }
  .footer-contact { font-size: 11px; line-height: 19px; margin-top: 3px; }
  .letterhead-arc { position: absolute; left: 0; bottom: 0; width: 692px; height: 21px; display: block; }
</style>
</head>
<body>

  <section class="logo-showcase" aria-label="Logo">
    <div class="wordmark">Atelier of Marwick<br>Beauty College</div>
  </section>

  <section class="business-card" aria-label="Business card">
    <div class="wordmark">Atelier of Marwick<br>Beauty College</div>
    <p class="card-name">Maren Holt</p>
    <p class="card-role">Director</p>
    <p class="card-mobile">Mobile&nbsp; +447700900418</p>
    <div class="card-rule"></div>
    <p class="card-company">Atelier of Marwick Beauty College</p>
    <p class="card-contact">
      Telephone 055501230148 Facsimile 055501230149<br>
      Address 214 Brindle Road, Ashcombe, Leicester, LE9 4QX, England<br>
      Email maren@amwbc.example Website www.atelierofmarwick.example
    </p>
    <svg class="card-arc" viewBox="0 0 295 10" preserveAspectRatio="none" aria-hidden="true">
      <path d="M0 10 Q147.5 -9 295 10 Z" fill="var(--gold)"/>
    </svg>
  </section>

  <section class="letterhead" aria-label="Letterhead">
    <div class="letterhead-logo">
      <div class="wordmark">Atelier of Marwick<br>Beauty College</div>
    </div>
    <footer class="letterhead-footer">
      <p class="footer-company">Atelier of Marwick Beauty College</p>
      <p class="footer-contact">
        Telephone 055501230148 Facsimile 055501230149 Address 214 Brindle Road, Ashcombe, Leicester, LE9 4QX, England<br>
        Email maren@amwbc.example Website www.atelierofmarwick.example
      </p>
    </footer>
    <svg class="letterhead-arc" viewBox="0 0 692 21" preserveAspectRatio="none" aria-hidden="true">
      <path d="M0 21 Q346 -20 692 21 Z" fill="var(--gold)"/>
    </svg>
  </section>

</body>
</html>
```